New Crowdfunding site Fundlark needs banner ads

I’m looking for 4 standard size banner ads for www.fundlark.example to be used by LinkaDeal Affiliates in order to bring new crowdfunding projects to the platform.
728x90
160x600
300x250
180x160

Succesful designers will put on our Mentors list so that the project owner can also get their specific project banners from our designers. Designers can also become our affiliates either to promote Fundlark.example or individual projects.
Updates

Please note updated brief

Thank you to those that have submitted designs so far.
Please be reminded that the invitation will close tomorrow after which we will make our choice

Thanks for input so far.
Please note project closes tomorrow (Sunday) after which we will choose.

Target Market(s)

Target is a project owner with a project requiring $10,000 or more in any field including business and/or non-profits. Any country.
Inventors, creatives, communities, hardware or software, consumer items,

Industry/Entity Type

Crowdfunding

Font styles to use
Sans Serif

Requirements
Must have
• Clear button call to action based on our USPs shown on the home page but especially the use of Affiliate Networks to promote their project to the widest possible audience.

Text and button text should be editable (see png preference).
Call to action could be based on "Free Crowdfunding Consultation - is your project viable" or "Get Your Free Guide to Succesful Crowdfunding"
Nice to have
• .png format preferred with separate objects.
Some animation preferred in the button.

```html
<!DOCTYPE html>
<html lang="en">
<head>
<meta charset="utf-8">
<title>Fundlark Banner Set</title>
<link href="https://fonts.googleapis.com/css2?family=Source+Sans+3:wght@400;600;700&display=swap" rel="stylesheet">
<style>
  :root {
    --sky-light: #eaf7fd;
    --sky-mid: #c8eafa;
    --sky-deep: #97d4f3;
    --accent-green: #2fae4a;
    --accent-navy: #2a4a9a;
    --accent-purple: #b066b0;
    --skyline-green: #3db34a;
    --ground-purple: #b86fb4;
    --brand-blue: #4a55a2;
    --text-dark: #1c1c1c;
    --button-deep: #0d2a6b;
    --button-mid: #2f63c4;
    --button-rim: #c9ced6;
    --button-text: #d4202a;
    --page: #ffffff;
  }
  * { box-sizing: border-box; margin: 0; padding: 0; }
  html, body { width: 1200px; height: 1195px; overflow: hidden; background: var(--page); }
  body { position: relative; font-family: "Source Sans 3", Arial, sans-serif; color: var(--text-dark); }

  .banner {
    position: absolute; overflow: hidden;
    background: linear-gradient(90deg, var(--sky-light) 0%, var(--sky-mid) 55%, var(--sky-deep) 100%);
  }
  .banner--skyscraper { left: 24px; top: 24px; width: 258px; height: 952px; }
  .banner--rectangle { left: 349px; top: 24px; width: 480px; height: 400px; }
  .banner--small { left: 445px; top: 496px; width: 288px; height: 256px; }
  .banner--leaderboard { left: 35px; top: 1021px; width: 1157px; height: 144px; }

  .masthead { position: absolute; left: 0; top: 0; background: var(--page); }
  .accent-band {
    position: absolute;
    background: linear-gradient(180deg, rgba(47,174,74,0.35) 0%, rgba(42,74,154,0.35) 50%, rgba(176,102,176,0.35) 100%);
  }
  .accent-band--vertical {
    background: linear-gradient(90deg, rgba(47,174,74,0.35) 0%, rgba(42,74,154,0.35) 50%, rgba(176,102,176,0.35) 100%);
  }

  .brand {
    position: absolute; display: flex; align-items: center;
    color: var(--brand-blue); font-weight: 600; letter-spacing: 0.5px; white-space: nowrap;
  }
  .brand__dot { border-radius: 50%; background: var(--accent-purple); flex: none; }

  .headline { position: absolute; text-align: center; font-weight: 400; line-height: 1.45; }

  .cta {
    position: absolute; display: flex; align-items: center; justify-content: center;
    border-radius: 14px; border: 4px solid var(--button-rim);
    background: linear-gradient(180deg, #6f9be6 0%, var(--button-mid) 35%, var(--button-deep) 100%);
    box-shadow: 0 2px 4px rgba(0,0,0,0.35);
    color: var(--button-text); font-weight: 700; letter-spacing: 0.3px; white-space: nowrap;
  }

  .skyline { position: absolute; left: 0; width: 100%; background: var(--skyline-green); }
  .ground { position: absolute; left: 0; width: 100%; bottom: 0; background: var(--ground-purple); }

  .photo-area {
    position: absolute; left: 0; width: 100%;
    background: radial-gradient(ellipse at 50% 70%, #b5b3a5 0%, #9aa67a 35%, rgba(160,200,215,0) 75%);
  }
</style>
</head>
<body>

  <section class="banner banner--skyscraper">
    <div class="masthead" style="width:258px; height:112px;"></div>
    <div class="accent-band" role="img" aria-label="Decorative header band" style="left:0; top:112px; width:258px; height:30px;"></div>
    <div class="brand" style="left:60px; top:44px; font-size:22px; gap:8px;">
      <span class="brand__dot" style="width:20px; height:20px;"></span>Fundlark
    </div>
    <p class="headline" style="left:0; top:294px; width:258px; font-size:33px;">Get Your<br>Free Guide<br>to<br>Successful<br>Crowdfunding</p>
    <div class="photo-area" role="img" aria-label="Green seedling growing from a pile of coins" style="top:596px; height:230px;"></div>
    <div class="cta" style="left:11px; top:840px; width:237px; height:54px; font-size:25px; color:var(--button-text); background:linear-gradient(180deg,#ffffff 0%,#cfe0f7 100%);">DON’T DELAY</div>
    <div class="skyline" role="img" aria-label="City skyline silhouette" style="top:912px; height:24px;"></div>
    <div class="ground" style="height:16px;"></div>
  </section>

  <section class="banner banner--rectangle">
    <div class="masthead" style="width:480px; height:112px;"></div>
    <div class="accent-band" role="img" aria-label="Decorative header band" style="left:0; top:112px; width:480px; height:26px;"></div>
    <div class="brand" style="left:30px; top:38px; font-size:26px; gap:10px;">
      <span class="brand__dot" style="width:24px; height:24px;"></span>Fundlark
    </div>
    <p class="headline" style="left:0; top:176px; width:480px; font-size:32px;">Get Your Free Guide to<br>Successful Crowdfunding</p>
    <div class="cta" style="left:115px; top:293px; width:251px; height:54px; font-size:25px; background:linear-gradient(180deg,#ffffff 0%,#cfe0f7 100%);">DON’T DELAY</div>
    <div class="skyline" role="img" aria-label="City skyline silhouette" style="top:362px; height:24px;"></div>
    <div class="ground" style="height:14px;"></div>
  </section>

  <section class="banner banner--small">
    <div class="masthead" style="width:288px; height:70px;"></div>
    <div class="accent-band" role="img" aria-label="Decorative header band" style="left:0; top:70px; width:288px; height:16px;"></div>
    <div class="brand" style="left:16px; top:20px; font-size:17px; gap:6px;">
      <span class="brand__dot" style="width:15px; height:15px;"></span>Fundlark
    </div>
    <p class="headline" style="left:0; top:112px; width:288px; font-size:19px;">Get Your Free Guide to<br>Successful Crowdfunding</p>
    <div class="cta" style="left:70px; top:186px; width:149px; height:35px; font-size:16px; border-width:3px; border-radius:10px; background:linear-gradient(180deg,#ffffff 0%,#cfe0f7 100%);">DON’T DELAY</div>
    <div class="skyline" role="img" aria-label="City skyline silhouette" style="top:234px; height:12px;"></div>
    <div class="ground" style="height:10px;"></div>
  </section>

  <section class="banner banner--leaderboard">
    <div class="masthead" style="width:370px; height:144px;"></div>
    <div class="accent-band accent-band--vertical" role="img" aria-label="Decorative side band" style="left:370px; top:0; width:36px; height:144px;"></div>
    <div class="brand" style="left:50px; top:48px; font-size:40px; gap:14px;">
      <span class="brand__dot" style="width:38px; height:38px;"></span>Fundlark
    </div>
    <p class="headline" style="left:420px; top:12px; width:430px; font-size:33px; line-height:1.4;">Get Your Free Guide to<br>Successful Crowdfunding</p>
    <div class="cta" style="left:868px; top:27px; width:254px; height:62px; font-size:27px; background:linear-gradient(180deg,#ffffff 0%,#cfe0f7 100%);">DON’T DELAY</div>
    <div class="skyline" role="img" aria-label="City skyline silhouette" style="left:406px; width:751px; top:118px; height:18px;"></div>
    <div class="ground" style="left:406px; width:751px; height:8px;"></div>
  </section>

</body>
</html>
```